Door Hanger Design for Electricians Serving Homes

I would like our logo incorporated into the door hanger. We would like a place for a tear off section on the bottom of the hanger with our contact information: K&T Electric - (555) 318-4702 - www.kandtelectric.example - info@kandtelectric.example.
Door Hanger Script
Front Side of the Door Hanger:
[Company Logo]
Need a Reliable Electrician?
Your Local Electrical Expert is Just Around the Corner!
• Quick Response Times
• Affordable Rates
• Quality Workmanship
• Fully Licensed & Insured
• Special Offer:
• 10% OFF Your First Service Call!
Back Side of the Door Hanger:
Don't Let Electrical Issues Keep You in the Dark!
From flickering lights to complete system upgrades, we've got all your
residential electrical needs covered. Our services include:
• Electrical Repairs & Troubleshooting
• Lighting Installation & Upgrades
• Safety Inspections & Code Compliance
• Energy-Efficient Solutions
• 24/7 Emergency Services
• Why Choose Us?
• Friendly, Local Service
• Over 30 Years of Experience
• Satisfaction Guaranteed
• Upfront Pricing
Call Us Today: [Your Phone Number]
Visit Our Website: [Your Website]
Book Your Appointment Now and Claim Your 10% Discount!
Offer valid for new customers on the first visit only. Mention this door hanger when
booking.
[Your Company Name and Contact Information]
Follow Us on Social Media for More Tips and Special Offers!
[Icons for social media platforms: Chatterpage, Pixmosaic, Quibbler, etc.]
Design Tips:
Use bold, clear fonts for easy reading.
Incorporate your brand colors and logo for instant recognition.
Include a clear call to action (CTA) on both sides.
Add a tear-off section at the bottom with your contact information for
convenience.
Use high-quality images or graphics related to electrical work to catch
the eye.
This door hanger design and copy aim to attract residential clients by
highlighting the benefits of your electrical services, special offers, and
how they can easily get in touch with you for their electrical needs.
The door knocker template will have three of the same design on front and three of the same design on the back. This template is from the print shop.

```html
<!DOCTYPE html>
<html lang="en">
<head>
<meta charset="utf-8">
<title>K&amp;T Electric Door Hanger</title>
<link rel="stylesheet" href="https://fonts.googleapis.com/css2?family=Anton&family=Montserrat:wght@500;700;800&family=Oswald:wght@400;500;600;700&display=swap">
<style>
:root{
  --stage:#8e8e8e;
  --red:#e0161b;
  --red-deep:#b30c10;
  --ink:#161616;
  --paper:#ffffff;
  --panel:#f1f1f1;
  --rule:#9a9a9a;
}
*{box-sizing:border-box;margin:0;padding:0}
html,body{width:1200px;height:2543px;overflow:hidden;background:var(--stage)}
.canvas{position:relative;width:1200px;height:2543px}
.hanger{position:absolute;top:730px;width:466px;height:1083px;background:var(--paper);overflow:hidden;box-shadow:6px 8px 14px rgba(0,0,0,.35)}
.hanger.front{left:116px}
.hanger.back{left:634px}
.abs{position:absolute}
.hole{position:absolute;left:170px;top:80px;width:126px;height:126px;border-radius:50%;background:var(--stage);box-shadow:inset 3px 4px 8px rgba(0,0,0,.45);z-index:5}
.slit{position:absolute;height:3px;background:#2a2a2a;transform-origin:left center;z-index:4}

/* front */
.front .photo{left:0;top:0;width:466px;height:588px;background:linear-gradient(160deg,#5a6a7a 0%,#c9ced4 35%,#e7e2d8 60%,#d9a85a 80%,#b9bcc0 100%)}
.brand{left:88px;top:455px;font-family:"Oswald",sans-serif;font-weight:700;color:var(--ink);font-size:40px;line-height:1;z-index:3}
.brand small{display:block;font-size:20px;margin-top:6px;font-weight:700}
.front .redline{left:0;top:588px;width:466px;height:8px;background:linear-gradient(90deg,var(--red) 60%,var(--ink) 60%)}
.kicker{left:0;width:466px;text-align:center;top:618px;font-family:"Oswald",sans-serif;font-weight:700;font-size:38px;line-height:1;color:var(--ink);letter-spacing:.5px}
.headline{left:0;width:466px;text-align:center;top:654px;font-family:"Anton",sans-serif;font-weight:400;font-size:80px;line-height:1;color:var(--red);text-shadow:2px 3px 0 rgba(0,0,0,.15)}
.tagline{left:0;width:466px;text-align:center;top:748px;font-family:"Oswald",sans-serif;font-weight:500;font-size:17px;line-height:1;color:var(--ink)}
.dots{left:22px;width:422px;top:776px;border-top:2px dotted var(--rule)}
.benefits{left:40px;top:792px;width:400px;display:grid;grid-template-columns:214px 186px;row-gap:12px;font-family:"Montserrat",sans-serif;font-weight:500;font-size:17px;line-height:1.2;color:var(--ink)}
.benefits li,.services li{list-style:none;position:relative;padding-left:26px}
.bolt{position:absolute;left:0;top:3px;width:18px;height:12px}
.vdiv{left:232px;top:790px;height:96px;border-left:1px solid var(--rule)}
.redbase{left:0;bottom:0;width:466px;height:148px;background:linear-gradient(180deg,var(--red) 0%,var(--red-deep) 100%)}
.redbase::after{content:"";position:absolute;left:0;bottom:0;width:100%;height:6px;background:var(--red)}
.offer{left:40px;top:905px;width:386px;height:106px;background:var(--panel);border:1px solid #c4c4c4}
.offer .tab{position:absolute;left:90px;top:-4px;width:226px;height:26px;background:var(--ink);color:#fff;font-family:"Montserrat",sans-serif;font-weight:700;font-size:19px;text-align:center;line-height:26px;clip-path:polygon(0 0,100% 0,92% 100%,8% 100%)}
.offer .big{position:absolute;left:12px;top:34px;font-family:"Montserrat",sans-serif;font-weight:800;font-size:50px;color:var(--red);line-height:1}
.offer .sep{position:absolute;left:252px;top:36px;height:46px;border-left:2px solid var(--ink)}
.offer .note{position:absolute;left:262px;top:38px;font-family:"Oswald",sans-serif;font-weight:600;font-size:17px;line-height:1.15;color:var(--ink)}
.contact{left:0;width:466px;text-align:center;color:#fff;font-family:"Montserrat",sans-serif;line-height:1.1}
.contact .ico{display:inline-block;vertical-align:middle;margin-right:6px}
.phone{font-weight:800;font-size:26px}
.web{font-weight:500;font-size:25px}

/* back */
.sec-title{left:47px;top:222px;font-family:"Anton",sans-serif;font-size:34px;line-height:1.2;color:var(--ink);letter-spacing:.5px}
.sec-title span{color:var(--red)}
.services{left:47px;top:270px;width:230px;font-family:"Oswald",sans-serif;font-weight:500;font-size:18px;line-height:1.3;color:var(--ink)}
.services li{padding-left:30px;padding-bottom:7px;margin-bottom:8px;border-bottom:1px dotted var(--rule)}
.services li:last-child{border-bottom:0}
.mascot{left:282px;top:200px;width:168px;height:345px;border-radius:40px 40px 8px 8px;background:linear-gradient(180deg,#2f6fa8 0%,#f2c14a 35%,#f2c14a 55%,#3a6a9a 75%,#6b3a22 100%)}
.back .redline{left:0;top:545px;width:466px;height:8px;background:linear-gradient(180deg,var(--red) 60%,var(--ink) 60%)}
.why{left:28px;top:567px;width:410px;height:315px;border:1px dashed #555}
.why .tab{position:absolute;left:36px;top:0;width:336px;height:38px;background:var(--red);color:#fff;font-family:"Oswald",sans-serif;font-weight:700;font-size:31px;line-height:38px;text-align:center;clip-path:polygon(0 0,100% 0,92% 100%,8% 100%)}
.why .line{position:absolute;left:0;width:100%;text-align:center;font-family:"Oswald",sans-serif;line-height:1.2}
.why .l1{top:42px;font-size:17px;font-weight:500;color:var(--ink)}
.why .l2{top:64px;font-size:30px;font-weight:400;color:var(--red)}
.why .l2 b{font-weight:700}
.why .l3{top:104px;font-size:25px;font-weight:500;color:var(--ink)}
.why .l4{top:138px;font-size:16px;font-weight:500;color:var(--red)}
.why .scene{position:absolute;left:8px;top:162px;width:392px;height:148px;background:radial-gradient(ellipse at 50% 80%,#e86a1c 0%,#f4a86a 45%,#fbe5d4 80%,#fff 100%)}
.back .redbase{height:155px}
.book{left:40px;top:890px;width:386px;height:86px;background:var(--panel);border:1px solid #c4c4c4}
.book .tab{position:absolute;left:20px;top:0;width:346px;height:24px;background:var(--ink);color:#fff;font-family:"Oswald",sans-serif;font-weight:500;font-size:14px;text-align:center;line-height:24px;clip-path:polygon(0 0,100% 0,95% 100%,5% 100%)}
.book .big{position:absolute;left:0;width:100%;top:34px;text-align:center;font-family:"Montserrat",sans-serif;font-weight:800;font-size:38px;color:var(--red);line-height:1}
.social{left:0;width:466px;text-align:center;top:1042px;color:#fff;font-family:"Montserrat",sans-serif;font-weight:500;font-size:10px;line-height:1.2;letter-spacing:.3px}
</style>
</head>
<body>
<main class="canvas">
  <svg width="0" height="0" style="position:absolute">
    <defs>
      <symbol id="bolt" viewBox="0 0 18 12"><path d="M0 1 L9 6 L8 3 L18 11 L9 8 L10 10 Z" fill="#e0161b"/></symbol>
      <symbol id="phone" viewBox="0 0 20 20"><path d="M5 2 L8 2 L9 6 L7 8 Q9 12 12 13 L14 11 L18 12 L18 15 Q18 18 15 18 Q3 17 2 5 Q2 2 5 2 Z" fill="none" stroke="#fff" stroke-width="1.8"/></symbol>
      <symbol id="globe" viewBox="0 0 20 20"><g fill="none" stroke="#fff" stroke-width="1.6"><circle cx="10" cy="10" r="8"/><ellipse cx="10" cy="10" rx="3.5" ry="8"/><path d="M2 10 H18"/></g></symbol>
    </defs>
  </svg>

  <!-- Front side -->
  <section class="hanger front">
    <div class="abs photo" role="img" aria-label="Photo of a hand testing wiring in an electrical panel with a red probe"></div>
    <div class="slit" style="left:100px;top:20px;width:190px;transform:rotate(38deg)"></div>
    <div class="hole"></div>
    <div class="abs brand">K&amp;T<small>ELECTRIC, LLC</small></div>
    <div class="abs redline"></div>
    <h2 class="abs kicker">NEED A RELIABLE</h2>
    <h1 class="abs headline">ELECTRICIAN?</h1>
    <p class="abs tagline">Your Local Electrical Expert is Just Around the Corner!</p>
    <div class="abs dots"></div>
    <div class="abs vdiv"></div>
    <ul class="abs benefits">
      <li><svg class="bolt"><use href="#bolt"/></svg>Quick Response<br>Times</li>
      <li><svg class="bolt"><use href="#bolt"/></svg>Quality<br>Workmanship</li>
      <li><svg class="bolt"><use href="#bolt"/></svg>Affordable<br>Rates</li>
      <li><svg class="bolt"><use href="#bolt"/></svg>Fully Licensed<br>&amp; Insured</li>
    </ul>
    <div class="abs redbase"></div>
    <div class="abs offer">
      <div class="tab">SPECIAL OFFER</div>
      <div class="big">10% OFF</div>
      <div class="sep"></div>
      <div class="note">YOUR FIRST<br>SERVICE CALL!</div>
    </div>
    <p class="abs contact phone" style="top:1018px"><svg class="ico" width="20" height="20"><use href="#phone"/></svg>(555) 318-4702</p>
    <p class="abs contact web" style="top:1050px"><svg class="ico" width="16" height="16"><use href="#globe"/></svg>www.kandtelectric.example</p>
  </section>

  <!-- Back side -->
  <section class="hanger back">
    <div class="slit" style="left:266px;top:68px;width:140px;transform:rotate(-40deg)"></div>
    <div class="hole"></div>
    <h2 class="abs sec-title">OUR <span>SERVICES</span></h2>
    <ul class="abs services">
      <li><svg class="bolt"><use href="#bolt"/></svg>Electrical Repairs &amp; Troubleshooting</li>
      <li><svg class="bolt"><use href="#bolt"/></svg>Lighting Installation &amp; Upgrades</li>
      <li><svg class="bolt"><use href="#bolt"/></svg>Safety Inspections &amp; Code Compliance</li>
      <li><svg class="bolt"><use href="#bolt"/></svg>Energy-Efficient Solutions</li>
      <li><svg class="bolt"><use href="#bolt"/></svg>24/7 Emergency Services</li>
    </ul>
    <div class="abs mascot" role="img" aria-label="Cartoon electrician in cap and overalls giving a thumbs up"></div>
    <div class="abs redline"></div>
    <div class="abs why">
      <div class="tab">WHY CHOOSE US?</div>
      <p class="line l1">FRIENDLY, LOCAL SERVICE</p>
      <p class="line l2">OVER <b>30 YEARS</b> OF <b>EXPERIENCE</b></p>
      <p class="line l3">SATISFACTION GUARANTEED</p>
      <p class="line l4">UPFRONT PRICING</p>
      <div class="scene" role="img" aria-label="Silhouettes of two electricians working at a control panel against an orange industrial backdrop"></div>
    </div>
    <div class="abs redbase"></div>
    <div class="abs book">
      <div class="tab">Book Your Appointment Now and Claim Your</div>
      <div class="big">10% DISCOUNT!</div>
    </div>
    <p class="abs contact phone" style="top:986px;font-size:25px"><svg class="ico" width="18" height="18"><use href="#phone"/></svg>(555) 318-4702</p>
    <p class="abs contact web" style="top:1014px;font-size:24px"><svg class="ico" width="14" height="14"><use href="#globe"/></svg>www.kandtelectric.example</p>
    <p class="abs social">Quibbler · Chatterpage · Pixmosaic</p>
  </section>
</main>
</body>
</html>
```